Health & Wellness Contest - The Bright Harvest Renewal

We need a postcard design that is professional and grabs the attention of people who see it. The postcard will be left in fitness centers and posted on social media. The front of the card MUST look amazing - make potential participants want to pick it up and find out more information; the back of the card will have the contest details. The goal is to have people sign up for a 90 day fitness program, and most of the marketing will be with this postcard.

Target Market(s)

People that are thinking about beginning a health regiment; people who are already used to exercising and are willing to try a new supplement

Industry/Entity Type

Health And Wellness

Colors

Designer to choose colors to be used in the design.

Requirements
Must have
• Front Cover -- Must have the phrase "The Bright Harvest Renewal" and must have "$2,500 Grand Prize"; and must have "BrightHarvestRenewal.com"
Nice to have
• Design on Front; Details on Back; appeal to both men and women

```html
<!DOCTYPE html>
<html lang="en">
<head>
<meta charset="utf-8">
<title>The Bright Harvest Renewal – Postcard</title>
<link rel="stylesheet" href="https://fonts.googleapis.com/css2?family=Anton&family=Alfa+Slab+One&family=Lato:wght@400;700&family=Montserrat:wght@800&display=swap">
<style>
  :root{
    --navy:#1d4f8f;
    --navy-deep:#163d70;
    --ink:#0e0e0f;
    --concrete:#e3e3e3;
    --concrete-dark:#cfcfcf;
    --paper:#ffffff;
    --stage:#ebebeb;
    --stamp:#6e6e6e;
    --rule:#8a8a8a;
    --text:#1a1a1a;
  }
  *{box-sizing:border-box;margin:0;padding:0}
  html,body{width:1200px;height:1200px;overflow:hidden}
  body{background:var(--stage);position:relative;font-family:'Lato',sans-serif;color:var(--text)}

  .postcard{position:absolute;left:270px;width:660px;height:512px;overflow:hidden;background:var(--paper)}
  .postcard--front{top:44px}
  .postcard--back{top:636px}
  .postcard svg.card-art{position:absolute;inset:0;width:100%;height:100%;display:block}

  /* front */
  .sponsor{position:absolute;left:0;width:372px;top:40px;display:flex;justify-content:center;align-items:center;gap:8px}
  .sponsor__mark{width:14px;height:14px;background:var(--navy)}
  .sponsor__name{font-family:'Lato',sans-serif;font-weight:700;font-size:13px;letter-spacing:1.6px;color:var(--navy-deep)}

  /* back */
  .back-title{position:absolute;left:25px;top:18px;font-family:'Montserrat',sans-serif;font-weight:800;font-size:25px;line-height:30px;color:var(--navy);letter-spacing:-0.3px;white-space:nowrap}
  .mission{position:absolute;left:22px;top:50px;width:150px;text-align:center;font-size:12px;line-height:15px}
  .intro{position:absolute;left:25px;top:160px;width:220px;font-size:12.5px;line-height:15px}
  .benefits{position:absolute;list-style:none;font-size:13px}
  .benefits li{height:23px;display:flex;align-items:center;gap:5px;white-space:nowrap}
  .benefits--left{left:23px;top:224px}
  .benefits--right{left:193px;top:233px}
  .benefits svg{width:13px;height:13px;flex:none;fill:var(--navy)}
  .benefits-divider{position:absolute;left:177px;top:230px;width:1px;height:102px;background:var(--ink)}
  .sponsor-contact{position:absolute;left:26px;top:378px;width:300px;color:var(--paper);font-size:14.5px;line-height:18px}
  .deadline{position:absolute;left:40px;width:230px;top:466px;text-align:center;color:var(--paper);font-size:13px;line-height:16px}
</style>
</head>
<body>

<section class="postcard postcard--front" aria-label="Postcard front">
  <svg class="card-art" viewBox="0 0 660 512">
    <defs>
      <linearGradient id="concreteFill" x1="0" y1="0" x2="1" y2="1">
        <stop offset="0" stop-color="#ededed"/>
        <stop offset="1" stop-color="#d3d3d3"/>
      </linearGradient>
      <linearGradient id="athletePhoto" x1="1" y1="0" x2="0.2" y2="1">
        <stop offset="0" stop-color="#2f5775"/>
        <stop offset="0.35" stop-color="#1c1e22"/>
        <stop offset="0.7" stop-color="#5a3a2a"/>
        <stop offset="1" stop-color="#1a1a1c"/>
      </linearGradient>
    </defs>

    <rect class="concrete" width="660" height="512" fill="url(#concreteFill)"/>

    <polygon class="athlete-photo" role="img" aria-label="Photo of an athletic woman in black sportswear holding dumbbells against a dark backdrop with blue smoke" points="338,0 660,0 660,512 462,512 452,402" fill="url(#athletePhoto)"/>

    <polygon class="accent-stripe" points="306,0 338,0 452,402 426,410" fill="var(--navy)"/>
    <polyline class="accent-edge" points="306,0 312,40 318,62 322,98 330,130 336,170 346,205 352,240 362,272 372,310 384,345 394,372 404,395 426,410" fill="none" stroke="var(--navy-deep)" stroke-width="4" stroke-linejoin="bevel"/>

    <polygon class="footer-band" points="0,494 426,400 452,402 462,512 0,512" fill="var(--navy)"/>
    <polyline class="footer-edge" points="0,494 40,484 62,488 96,474 130,470 160,460 196,456 230,444 262,440 296,428 330,424 362,414 396,410 426,400" fill="none" stroke="var(--ink)" stroke-width="5" stroke-linejoin="bevel"/>

    <text class="title-vertical" transform="translate(116,330) rotate(-90)" font-family="'Alfa Slab One', serif" font-size="52" fill="var(--navy)" textLength="236" lengthAdjust="spacingAndGlyphs">Renewal</text>
    <text class="title-the" x="128" y="186" font-family="Anton, sans-serif" font-size="118" fill="var(--ink)" textLength="168" lengthAdjust="spacingAndGlyphs">THE</text>
    <text class="title-bright" x="130" y="248" font-family="Anton, sans-serif" font-size="60" fill="var(--navy)" textLength="166" lengthAdjust="spacingAndGlyphs">BRIGHT</text>
    <text class="title-harvest" x="128" y="320" font-family="Anton, sans-serif" font-size="84" fill="var(--ink)" textLength="200" lengthAdjust="spacingAndGlyphs">HARVEST</text>

    <polygon class="ribbon-tail" points="17,330 60,330 60,384 28,384 40,356" fill="var(--navy)"/>
    <polygon class="ribbon-tail" points="380,330 337,330 337,384 369,384 357,356" fill="var(--navy)"/>
    <rect class="prize-banner" x="34" y="336" width="329" height="48" fill="var(--ink)"/>
    <text class="prize-text" x="198" y="373" text-anchor="middle" font-family="Anton, sans-serif" font-size="32" fill="#ffffff" textLength="292" lengthAdjust="spacingAndGlyphs">$2,500 GRAND PRIZE</text>

    <text class="web-address" x="212" y="490" text-anchor="middle" font-family="Lato, sans-serif" font-size="17" fill="#ffffff">BrightHarvestRenewal.com</text>
  </svg>

  <div class="sponsor">
    <span class="sponsor__mark"></span>
    <span class="sponsor__name">RIDGELINE LAW GROUP</span>
  </div>
</section>

<section class="postcard postcard--back" aria-label="Postcard back">
  <svg class="card-art" viewBox="0 0 660 512">
    <defs>
      <linearGradient id="couplePhoto" x1="0" y1="0" x2="0" y2="1">
        <stop offset="0" stop-color="#2a2b2e"/>
        <stop offset="0.55" stop-color="#6b4a38"/>
        <stop offset="1" stop-color="#ffffff"/>
      </linearGradient>
    </defs>
    <rect width="660" height="512" fill="var(--paper)"/>

    <polygon class="couple-photo" role="img" aria-label="Photo of a fit man and woman in black athletic wear standing side by side" points="188,0 388,0 410,110 422,205 252,205 236,120" fill="url(#couplePhoto)"/>

    <polygon class="corner-stripe" points="172,0 190,0 264,58 252,66" fill="var(--navy)"/>
    <polygon class="title-band" points="0,140 248,100 252,112 0,157" fill="var(--navy)"/>
    <polygon class="side-stripe" points="380,208 393,208 334,512 320,512" fill="var(--navy)"/>

    <line x1="0" y1="340" x2="332" y2="352" stroke="var(--navy)" stroke-width="3"/>
    <polygon class="contact-band" points="0,345 332,357 338,410 0,462" fill="var(--ink)"/>
    <polygon class="deadline-band" points="0,466 342,414 318,512 0,512" fill="var(--navy)"/>

    <rect class="stamp-box" x="533" y="69" width="77" height="83" fill="var(--stamp)"/>
    <g class="address-lines" stroke="var(--rule)" stroke-width="1">
      <line x1="411" y1="271" x2="620" y2="271"/>
      <line x1="411" y1="316" x2="620" y2="316"/>
      <line x1="411" y1="366" x2="620" y2="366"/>
    </g>
  </svg>

  <h2 class="back-title">The Bright</h2>
  <p class="mission">Harvest Renewal has one mission to help people be a better version of themselves</p>
  <p class="intro">Join us in the Bright Harvest Renewal and experience some of the benefits that countless others have seen:</p>

  <ul class="benefits benefits--left">
    <li><svg viewBox="0 0 16 16"><path d="M8 14.5 1.8 8.4A3.8 3.8 0 0 1 8 3.2a3.8 3.8 0 0 1 6.2 5.2Z"/></svg>Better health</li>
    <li><svg viewBox="0 0 16 16"><rect x="3" y="1" width="2" height="14"/><rect x="1" y="1" width="1.5" height="6"/><rect x="5.5" y="1" width="1.5" height="6"/><path d="M11 1c2 0 3 2 3 5s-1 4-2 4v5h-2V1Z"/></svg>Appetite suppression</li>
    <li><svg viewBox="0 0 16 16"><path d="M9 1 3 9h4l-1 6 6-8H8Z"/></svg>Better energy</li>
    <li><svg viewBox="0 0 16 16"><circle cx="8" cy="3" r="2"/><path d="M5 6h6l-1 5H6Z"/><rect x="6" y="11" width="1.6" height="4"/><rect x="8.4" y="11" width="1.6" height="4"/></svg>Fat Loss</li>
    <li><svg viewBox="0 0 16 16"><circle cx="8" cy="8" r="6.5" fill="none" stroke="#1d4f8f" stroke-width="1.4"/><circle cx="8" cy="8" r="3.5" fill="none" stroke="#1d4f8f" stroke-width="1.4"/><circle cx="8" cy="8" r="1.2"/></svg>Better focus</li>
  </ul>
  <div class="benefits-divider"></div>
  <ul class="benefits benefits--right">
    <li><svg viewBox="0 0 16 16"><path d="M8 1a5 5 0 0 0-3 9v2h6v-2a5 5 0 0 0-3-9Z"/><rect x="5.5" y="13" width="5" height="2"/></svg>Increased awareness</li>
    <li><svg viewBox="0 0 16 16"><circle cx="8" cy="8" r="6.5" fill="none" stroke="#1d4f8f" stroke-width="1.4"/><circle cx="5.8" cy="6.5" r="1"/><circle cx="10.2" cy="6.5" r="1"/><path d="M4.8 9.5a3.4 3.4 0 0 0 6.4 0" fill="none" stroke="#1d4f8f" stroke-width="1.3"/></svg>Better mood</li>
    <li><svg viewBox="0 0 16 16"><rect x="0.5" y="5" width="2.5" height="6"/><rect x="13" y="5" width="2.5" height="6"/><rect x="3" y="6.5" width="1.8" height="3"/><rect x="11.2" y="6.5" width="1.8" height="3"/><rect x="4.8" y="7.3" width="6.4" height="1.4"/></svg>Muscle preservation</li>
    <li><svg viewBox="0 0 16 16"><rect x="1" y="4" width="1.5" height="10"/><rect x="1" y="9" width="14" height="2.5"/><rect x="13.5" y="9" width="1.5" height="5"/><circle cx="5" cy="7" r="1.6"/><rect x="7" y="6" width="8" height="3"/></svg>Better sleep</li>
  </ul>

  <p class="sponsor-contact">For challenge details, email one of our sponsors at info@ridgelinelaw.org.</p>
  <p class="deadline">Challenge Deadline:<br>Register by October 31, 2017.</p>
</section>

</body>
</html>
```